Stationary design for real estate company in Trinidad and Tobago

Kestra Realty Ltd. , real estate company operating in Trinidad and Tobago, requires a sleek, modern and professional stationary package to wow our customers and potential new clients. we want to look sleek and professional; first impressions count in this business!
Business Address:
Level 1, Marlowe Point Tower
4C Seldon Grove Boulevard
Marlowe Point
Colwyn Pereira Highway
Port of Spain
Trinidad
Tel: + 1 868 555 0147
www.kestra-tt.com
info@kestra-tt.com

```html
<!DOCTYPE html>
<html lang="en">
<head>
<meta charset="utf-8">
<title>Kestra Realty – Stationery Package</title>
<link href="https://fonts.googleapis.com/css2?family=Lato:wght@300;400;700&family=Montserrat:wght@600;700&display=swap" rel="stylesheet">
<style>
:root{
  --navy:#1c3561;
  --gold:#c9a35e;
  --gold-light:#e2c78f;
  --paper:#ffffff;
  --globe:#eceef2;
  --text:#5a6070;
  --scene:#2c2e31;
  --board:#e3e4e6;
  --header:#e9eaec;
}
*{box-sizing:border-box;margin:0;padding:0}
html,body{width:1200px;height:2366px;overflow:hidden}
body{position:relative;font-family:'Lato',sans-serif;color:var(--text);background:var(--board)}
.abs{position:absolute}

.header-band{left:0;top:0;width:1200px;height:104px;background:linear-gradient(#f3f3f4,var(--header))}
.showcase{left:0;top:104px;width:1200px;height:870px;background:var(--scene)}
.board{left:0;top:974px;width:1200px;height:1392px;background:linear-gradient(180deg,#e8e9eb,#dfe0e2)}

.brand{display:flex;align-items:center;gap:.35em;font-family:'Lato',sans-serif;font-weight:400;color:var(--navy);letter-spacing:.06em;text-transform:uppercase;white-space:nowrap;line-height:1}
.brand .dot{width:.8em;height:.8em;border-radius:50%;background:var(--gold);flex:none}
.brand.light{color:#fff}
.brand.centered{justify-content:center}

.sheet{background:var(--paper);box-shadow:0 3px 8px rgba(0,0,0,.22);overflow:hidden}
.globe{position:absolute;border-radius:50%;background:radial-gradient(circle at 40% 40%,#f3f4f6 0%,var(--globe) 70%,#e4e6ea 100%)}
.base-bar{position:absolute;left:0;bottom:0;height:4px;background:var(--navy)}

.address{font-size:5.6px;line-height:1.35;color:var(--text)}
.address p+p{margin-top:5px}
.person{font-family:'Montserrat',sans-serif;font-weight:600;color:var(--gold);white-space:nowrap}
.person b{color:var(--navy);font-weight:700}
.role{color:var(--text)}
.contact{display:flex;align-items:center;gap:3px;white-space:nowrap;color:var(--text)}
.icon{display:block;flex:none}
.rule{height:1px;background:var(--gold)}
</style>
</head>
<body>

<svg width="0" height="0" style="position:absolute">
  <defs>
    <symbol id="ico-phone" viewBox="0 0 10 10"><rect width="10" height="10" rx="1.2" fill="#1c3561"/><path d="M3 2.2l1.2 1.5-.6.8a4 4 0 0 0 1.9 1.9l.8-.6L7.8 7 7 7.9C4.6 7.7 2.3 5.4 2.1 3z" fill="#fff"/></symbol>
    <symbol id="ico-mail" viewBox="0 0 10 10"><rect width="10" height="10" rx="1.2" fill="#1c3561"/><rect x="2" y="3" width="6" height="4.2" fill="#fff"/><path d="M2 3l3 2.3L8 3" fill="none" stroke="#1c3561" stroke-width=".6"/></symbol>
    <symbol id="ico-web" viewBox="0 0 10 10"><rect width="10" height="10" rx="1.2" fill="#1c3561"/><path d="M3.2 2.4L7.4 5.6 5.4 5.8 6.4 7.8 5.6 8.1 4.7 6.2 3.3 7.5z" fill="#fff"/></symbol>
    <symbol id="ico-phone-gold" viewBox="0 0 10 10"><rect width="10" height="10" rx="1.2" fill="#c9a35e"/><path d="M3 2.2l1.2 1.5-.6.8a4 4 0 0 0 1.9 1.9l.8-.6L7.8 7 7 7.9C4.6 7.7 2.3 5.4 2.1 3z" fill="#fff"/></symbol>
    <symbol id="ico-mail-gold" viewBox="0 0 10 10"><rect width="10" height="10" rx="1.2" fill="#c9a35e"/><rect x="2" y="3" width="6" height="4.2" fill="#fff"/><path d="M2 3l3 2.3L8 3" fill="none" stroke="#c9a35e" stroke-width=".6"/></symbol>
    <symbol id="ico-web-gold" viewBox="0 0 10 10"><rect width="10" height="10" rx="1.2" fill="#c9a35e"/><path d="M3.2 2.4L7.4 5.6 5.4 5.8 6.4 7.8 5.6 8.1 4.7 6.2 3.3 7.5z" fill="#fff"/></symbol>
    <symbol id="card-back" viewBox="0 0 267 159">
      <rect width="267" height="159" fill="#c9a35e"/>
      <rect x="150" width="117" height="159" fill="#1c3561"/>
      <circle cx="165" cy="120" r="140" fill="#1c3561"/>
      <circle cx="165" cy="128" r="130" fill="#20396a"/>
    </symbol>
  </defs>
</svg>

<!-- HEADER -->
<div class="abs header-band"></div>
<div class="abs brand centered" style="left:0;width:1200px;top:36px;font-size:30px">Kestra Realty</div>

<!-- SHOWCASE (flat) -->
<div class="abs showcase"></div>

<div class="abs sheet" style="left:110px;top:402px;width:460px;height:274px">
  <svg class="abs" style="left:0;top:0" width="460" height="274" viewBox="0 0 267 159"><use href="#card-back"/></svg>
  <div class="abs" role="img" aria-label="faint world globe map" style="left:110px;top:40px;width:320px;height:320px;border-radius:50%;background:radial-gradient(circle,rgba(255,255,255,.05),rgba(255,255,255,0) 70%)"></div>
  <div class="abs brand light centered" style="left:150px;width:290px;top:126px;font-size:22px"><span class="dot"></span>Kestra Realty</div>
</div>

<div class="abs sheet" style="left:630px;top:402px;width:460px;height:274px">
  <div class="globe" role="img" aria-label="faint world globe map" style="left:205px;top:28px;width:330px;height:330px"></div>
  <div class="abs brand" style="left:34px;top:36px;font-size:22px"><span class="dot"></span>Kestra Realty</div>
  <div class="abs address" style="left:34px;top:168px;font-size:9.5px">
    <p>Level 1, Marlowe Point Tower<br>4C Seldon Grove Boulevard<br>Marlowe Point</p>
    <p>Colwyn Pereira Highway<br>Port of Spain<br>Trinidad</p>
  </div>
  <div class="abs" style="right:34px;top:148px;text-align:right">
    <div class="person" style="font-size:13px">DANIEL R. <b>WHITCOMBE</b></div>
    <div class="role" style="font-size:10px;margin-top:2px">Managing Director</div>
    <div class="rule" style="width:60px;margin:5px 0 8px auto"></div>
    <div class="contact" style="font-size:10px;justify-content:flex-end">+ 1 868 555 0147<svg class="icon" width="12" height="12"><use href="#ico-phone"/></svg></div>
    <div class="contact" style="font-size:10px;justify-content:flex-end;margin-top:5px">info@kestra-tt.com<svg class="icon" width="12" height="12"><use href="#ico-mail"/></svg></div>
    <div class="contact" style="font-size:10px;justify-content:flex-end;margin-top:5px">www.kestra-tt.com<svg class="icon" width="12" height="12"><use href="#ico-web"/></svg></div>
  </div>
  <div class="base-bar" style="width:200px;height:6px"></div>
</div>

<!-- STATIONERY BOARD -->
<div class="abs board"></div>

<!-- business card front -->
<div class="abs sheet" style="left:48px;top:1020px;width:266px;height:159px">
  <div class="globe" role="img" aria-label="faint world globe map" style="left:104px;top:14px;width:200px;height:200px"></div>
  <div class="abs brand" style="left:19px;top:22px;font-size:13px"><span class="dot"></span>Kestra Realty</div>
  <div class="abs address" style="left:19px;top:92px">
    <p>Level 1, Marlowe Point Tower<br>4C Seldon Grove Boulevard<br>Marlowe Point</p>
    <p>Colwyn Pereira Highway<br>Port of Spain<br>Trinidad</p>
  </div>
  <div class="abs" style="right:19px;top:90px;text-align:right">
    <div class="person" style="font-size:7.2px">DANIEL R. <b>WHITCOMBE</b></div>
    <div class="role" style="font-size:5.6px;margin-top:1px">Managing Director</div>
    <div class="rule" style="width:34px;margin:3px 0 6px auto"></div>
    <div class="contact" style="font-size:5.6px;justify-content:flex-end">+ 1 868 555 0147<svg class="icon" width="7" height="7"><use href="#ico-phone"/></svg></div>
    <div class="contact" style="font-size:5.6px;justify-content:flex-end;margin-top:4px">info@kestra-tt.com<svg class="icon" width="7" height="7"><use href="#ico-mail"/></svg></div>
    <div class="contact" style="font-size:5.6px;justify-content:flex-end;margin-top:4px">www.kestra-tt.com<svg class="icon" width="7" height="7"><use href="#ico-web"/></svg></div>
  </div>
  <div class="base-bar" style="width:110px"></div>
</div>

<!-- business card back -->
<div class="abs sheet" style="left:350px;top:1020px;width:267px;height:159px">
  <svg class="abs" style="left:0;top:0" width="267" height="159" viewBox="0 0 267 159"><use href="#card-back"/></svg>
  <div class="abs brand light centered" style="left:90px;width:170px;top:72px;font-size:13px"><span class="dot"></span>Kestra Realty</div>
</div>

<!-- compliment slip -->
<div class="abs sheet" style="left:48px;top:1221px;width:569px;height:144px">
  <div class="globe" role="img" aria-label="faint world globe map" style="left:455px;top:40px;width:150px;height:150px"></div>
  <div class="abs brand" style="left:19px;top:68px;font-size:10px"><span class="dot"></span>Kestra Realty</div>
  <div class="abs" style="left:143px;top:36px">
    <div class="person" style="font-size:10.5px">DANIEL R. <b>WHITCOMBE</b></div>
    <div class="role" style="font-size:7.2px;margin-top:2px">Managing Director</div>
    <div class="rule" style="width:28px;margin:4px 0 6px"></div>
    <div class="contact" style="font-size:7.6px"><svg class="icon" width="9" height="9"><use href="#ico-phone"/></svg>+ 1 868 555 0147</div>
    <div class="contact" style="font-size:7.6px;margin-top:6px"><svg class="icon" width="9" height="9"><use href="#ico-mail"/></svg>info@kestra-tt.com</div>
    <div class="contact" style="font-size:7.6px;margin-top:6px"><svg class="icon" width="9" height="9"><use href="#ico-web"/></svg>www.kestra-tt.com</div>
  </div>
  <div class="abs address" style="left:242px;top:69px;font-size:7.4px">
    <p>Level 1, Marlowe Point Tower<br>4C Seldon Grove Boulevard, Marlowe Point</p>
    <p>Colwyn Pereira Highway<br>Port of Spain,Trinidad</p>
  </div>
  <div class="base-bar" style="width:456px"></div>
</div>

<!-- envelope -->
<div class="abs sheet" style="left:48px;top:1413px;width:568px;height:284px">
  <div class="globe" role="img" aria-label="faint world globe map" style="left:420px;top:152px;width:220px;height:220px"></div>
  <div class="abs brand" style="left:19px;top:27px;font-size:18px"><span class="dot"></span>Kestra Realty</div>
  <div class="abs address" style="left:19px;top:210px;font-size:9.6px">
    <p>Level 1, Marlowe Point Tower<br>4C Seldon Grove Boulevard, Marlowe Point</p>
    <p>Colwyn Pereira Highway<br>Port of Spain,Trinidad</p>
  </div>
  <div class="base-bar" style="width:422px"></div>
</div>

<!-- letterhead -->
<div class="abs sheet" style="left:652px;top:1023px;width:482px;height:674px">
  <div class="abs brand" style="left:16px;top:27px;font-size:14px"><span class="dot"></span>Kestra Realty</div>
  <div class="abs" style="left:16px;top:50px;width:466px;height:1px;background:#d9dbe0"></div>
  <div class="globe" role="img" aria-label="faint world globe map" style="left:310px;top:522px;width:210px;height:210px"></div>
  <div class="abs address" style="left:15px;top:615px;font-size:7.4px">
    <p>Level 1, Marlowe Point Tower<br>4C Seldon Grove Boulevard, Marlowe Point</p>
    <p>Colwyn Pereira Highway<br>Port of Spain, Trinidad</p>
  </div>
  <div class="abs" style="right:16px;top:613px">
    <div class="contact" style="font-size:8px;justify-content:flex-end">+ 1 868 555 0147<svg class="icon" width="10" height="10"><use href="#ico-phone"/></svg></div>
    <div class="contact" style="font-size:8px;justify-content:flex-end;margin-top:7px">info@kestra-tt.com<svg class="icon" width="10" height="10"><use href="#ico-mail"/></svg></div>
    <div class="contact" style="font-size:8px;justify-content:flex-end;margin-top:7px">www.kestra-tt.com<svg class="icon" width="10" height="10"><use href="#ico-web"/></svg></div>
  </div>
  <div class="base-bar" style="width:318px"></div>
</div>

<!-- presentation folder (flat die-line) -->
<svg class="abs" style="left:48px;top:1742px" width="683" height="562" viewBox="0 0 683 562">
  <defs>
    <clipPath id="folder-face"><rect x="26" y="0" width="629" height="420"/></clipPath>
    <radialGradient id="globe-fill" cx="0.4" cy="0.4" r="0.6"><stop offset="0" stop-color="#f4f5f7"/><stop offset="1" stop-color="#e8eaee"/></radialGradient>
  </defs>
  <path d="M26 311 L0 323 L0 414 L26 426 Z" fill="#fff" stroke="#c9cbd0" stroke-width=".6"/>
  <path d="M655 311 L681 323 L681 414 L655 426 Z" fill="#fff" stroke="#c9cbd0" stroke-width=".6"/>
  <path d="M26 420 L339 420 L335 560 L26 560 Z" fill="#fff" stroke="#c9cbd0" stroke-width=".6"/>
  <path d="M342 420 L655 420 L655 560 L346 560 Z" fill="#fff" stroke="#c9cbd0" stroke-width=".6"/>
  <g clip-path="url(#folder-face)">
    <rect x="26" y="0" width="629" height="420" fill="#fff"/>
    <rect x="26" y="0" width="320" height="420" fill="#1c3561"/>
    <circle cx="524" cy="289" r="343" fill="#fff"/>
    <circle cx="524" cy="289" r="330" fill="url(#globe-fill)" role="img" aria-label="faint world globe map"/>
  </g>
  <line x1="340" y1="0" x2="340" y2="420" stroke="#dfe1e5" stroke-width=".8"/>
</svg>
<div class="abs" style="left:112px;top:1786px;color:#fff;font-size:10.5px;line-height:1.3">
  <div class="contact" style="color:#fff;gap:6px"><svg class="icon" width="12" height="12"><use href="#ico-phone-gold"/></svg>+ 1 868 555 0147</div>
  <div class="contact" style="color:#fff;gap:6px;margin-top:8px"><svg class="icon" width="12" height="12"><use href="#ico-mail-gold"/></svg>info@kestra-tt.com</div>
  <div class="contact" style="color:#fff;gap:6px;margin-top:8px"><svg class="icon" width="12" height="12"><use href="#ico-web-gold"/></svg>www.kestra-tt.com</div>
  <p style="margin-top:14px;font-size:9.2px">Level 1, Marlowe Point Tower<br>4C Seldon Grove Boulevard<br>Marlowe Point</p>
  <p style="margin-top:10px;font-size:9.2px">Colwyn Pereira Highway<br>Port of Spain, Trinidad</p>
</div>
<div class="abs brand" style="left:432px;top:1935px;font-size:28px"><span class="dot"></span>Kestra Realty</div>

<!-- apparel mark (chest placement) -->
<div class="abs brand" style="left:975px;top:1930px;font-size:9px"><span class="dot"></span>Kestra Realty</div>

</body>
</html>
```